KELVARA OIL BROCHURE

Design a brochure for Kelvara Oil and Gas Limited using the attached information.
An Overview / Background of the Business & Services

Kelvara Oil and Gas Limited (KOGL) is an oil and gas company dually incorporated under the laws of the Federal Republic of Nigeria. KOGL operations cover both the upstream and downstream activities of the oil and gas industry.

The company is led by a team of seasoned professionals with an excess of 28 years combined hands-on and top management experience in the industry. This is in addition to the wealth of experience and technology of our affiliates and technical partners.

KOGL was started to provide excellent, cost efficient, effective solutions and specialized operations for the oil and gas industry. It stated as a service company providing solutions in the environmental sector and has progressed to provide a comprehensive range of solutions in engineering, production, procurement and maintenance services.

Our key strength is the expertise of our staff, the vast experience of our technical partners, our vision and our commitment to our core values.

We are here to serve you better.

Vision Statement
Our vision is to be the gas and oil company of excellence and global leader in this sector.

Mission Statement
Our mission is to achieve our vision in the shortest possible time.

=================
Operations

Services
Kelvara Oil and Gas Limited is functional in both the downstream and upstream operation. Whatever your need, we have the expertise to offer solutions and guidance.

Our wide array of services includes:
 Pipeline and flow lines design, construction/installation, maintenance and emergency repairs.
 Maintenance and rehabilitation of platforms, gas compressor plants and flow stations.
 Installation & maintenance of steam and gas turbines, boilers & heat exchangers, fire water system, pumps, etc.
 Installation & maintenance of booster pumps and platform refurbishment.
 Engineering Design Services.
 Procurement Services.
 Provide experienced and professional technical Manpower
 Engineering Services (Mechanical, Civil and Electrical works)
 Environmental Services

We can execute fully integrated projects at remote locations supported by a satellite office. Our team work diligently to maximize clients’ return and avoid unplanned downtime. We have the requisite equipment to deliver value and quality.

Products
Equipment Hire
We use state of the art equipment to deliver prompt services according to specifications. We also support the industry and grow local capacity by offering equipment hire and lease services. We have in stock an array of pre-mobbed equipment, ready to be deployed for emergency and planned activity.

Show pictures of equipment (See attached pictures)

Materials
In conjunction with our partners we offer the following materials:

=================
Project Portfolio
In have delivered a number of quality and durable projects.

Show pictures of work done. (See attached pictures)

=======================
Corporate Culture

Quality Culture
Kelvara Oil and Gas Limited pride itself on its corporate quality culture. We feel strongly that quality goes beyond simply following procedures and meeting productivity expectations.

At every level of the company, we insist on taking quality focused action and transferring those values to our clients. The culture of quality is part of our environment. The end result is better communication, high-end services and products that function as promised.

Each member of the Kelvara team is empowered and expected to make good decisions based on the need to deliver quality and value.

Health, Safety and Environment (HSE)
Health, Safety and Environment (HSE) is a fundamental component of KOGL business principles and corporate culture. It is our priority to maintain safe and healthy working conditions by ensuring industrial and work area safety rules, regulations, laws, conditions and standard codes.

The company believes that effective management of HSE affairs not only protects staff and environment, but also contributes to the company’s success. Therefore, we regard it as important as the achievement of any other key business objective.

Our Core Values
At Kelvara Oil and Gas Limited we aim to be good corporate citizens in every area of our operations. We mold our actions around a corporate value guide that is central to all our decision making policy.

Our values are based on a commitment to the greater good of our employees, clients, and the safety and protection of the environments where we work. Investing in communities and groups in ways that are aligned with our values is part of our corporate policy. In addition, it is our culture to restore integrity for every services and products under our care.

While we operate the professional best practices in the oil and gas industry, our overriding core values include:
 To conduct KOGL businesses to the glory and pleasure of the Almighty God.
 To express the righteousness of God in all operations, products and services as our brand.
 To treat our staff as valued partners (co-owner) in the business.
 To work in such a way that will preserve the earth resources.

Partners
Our strategic partners were carefully selected for their industry knowledge about local conditions and international trends. They have the ability to provide comprehensive, effective support to our client. As a result of these relationships, Kelvara Oil and Gas Limited is able to deliver innovative technical solutions to the localities where it operates.

We use these strategic partnerships to unlock value in projects worldwide. They enable us to provide the latest technology and resources for future projects. Together we are able to use the full potential of our mutual resources to provide values for our clients.

Partners:
www.plextrowave.example
www.morvidquel.example
www.haldin-prewett.example

Contact
Website: www.kelvaraoilandgas.example
E-mail: info@kelvaraoilandgas.example

Target Market(s)

The oil and gas community - oil and gas servicing companies, production companies, refinaries etc.

Industry/Entity Type

Business

Font styles to use
Serif
Script

Requirements
Must have
• Picture and photos. I have attached some pictures of completed work.
Nice to have
• Some nice photos from the net will be good

```html
<!DOCTYPE html>
<html lang="en">
<head>
<meta charset="utf-8">
<title>Kelvara Oil and Gas – Brochure Spread</title>
<link rel="stylesheet" href="https://fonts.googleapis.com/css2?family=Arimo:wght@400;700&family=Open+Sans:wght@400;600&display=swap">
<style>
:root{
  --bg:#8d8d8d;
  --paper:#ffffff;
  --navy:#1f3f8f;
  --blue:#2a5db8;
  --rule:#3b66b5;
  --ink:#3a3a3a;
  --green:#1d7a3a;
  --green-dark:#146030;
  --orange:#f08a1c;
  --tick:#2e9a3c;
}
*{box-sizing:border-box;margin:0;padding:0}
html,body{width:1200px;height:737px;overflow:hidden;background:var(--bg)}
body{font-family:"Open Sans",Arial,sans-serif;color:var(--ink)}
.spread{position:absolute;left:40px;top:18px;width:1120px;height:700px;display:flex;box-shadow:0 6px 20px rgba(0,0,0,.35)}
.page{position:relative;width:560px;height:700px;background:var(--paper);overflow:hidden}
.page--left{box-shadow:inset -14px 0 18px -14px rgba(0,0,0,.25)}
.page--right{box-shadow:inset 14px 0 18px -14px rgba(0,0,0,.25)}
.content{position:relative;z-index:2;padding:30px 34px 0}
h2{font-family:"Arimo",Arial,sans-serif;font-weight:700;color:var(--navy);font-size:17px;letter-spacing:.2px;text-transform:uppercase;padding-bottom:3px;border-bottom:1.5px solid var(--rule);margin:14px 0 6px}
h2:first-child{margin-top:0}
h3{font-family:"Arimo",Arial,sans-serif;font-weight:400;color:var(--blue);font-size:12px;margin:2px 0 4px}
p{font-size:8.6px;line-height:1.42;margin-bottom:6px;text-align:justify}
.values{list-style:none;margin:2px 0 8px 14px}
.values li{font-size:8.6px;line-height:1.42;color:var(--blue);position:relative;padding-left:10px}
.values li::before{content:"›";position:absolute;left:0;color:var(--blue)}
.photo-main{position:absolute;left:0;bottom:0;width:560px;height:380px;z-index:1;
  background:linear-gradient(180deg,rgba(255,255,255,1) 0%,rgba(214,224,236,.9) 28%,#9fb3c8 50%,#6f8aa6 70%,#2f6b48 88%,#1f5a36 100%)}
.services{display:grid;grid-template-columns:1fr 1fr;column-gap:18px;list-style:none;margin:4px 0 8px}
.services li{font-size:8.6px;line-height:1.38;position:relative;padding-left:14px;margin-bottom:5px}
.services li svg{position:absolute;left:0;top:1px;width:9px;height:9px}
.band{position:absolute;left:0;bottom:0;z-index:1}
.site-pill{position:absolute;z-index:3;left:266px;bottom:22px;width:230px;height:26px;border-radius:13px;background:var(--navy);border:2px solid #fff;color:#fff;font-family:"Arimo",Arial,sans-serif;font-size:12px;display:flex;align-items:center;justify-content:center}
</style>
</head>
<body>
<div class="spread">
  <section class="page page--left">
    <div class="photo-main" role="img" aria-label="Photo of a worker in green overalls and hard hat operating equipment at a gas processing plant"></div>
    <div class="content">
      <h2>Our Core Values</h2>
      <p>At Kelvara Oil and Gas Limited we aim to be good corporate citizens in every area of our operations. We mold our actions around a corporate value guide that is central to all our decision making policy.</p>
      <p>Our values are based on a commitment to the greater good of our employees, clients, and the safety and protection of the environments where we work. Investing in communities and groups in ways that are aligned with our values is part of our corporate policy. In addition, it is our culture to restore integrity for every services and products under our care.</p>
      <p>While we operate the professional best practices in the oil and gas industry, our overriding core values include:</p>
      <ul class="values">
        <li>To conduct KOGL businesses to the glory and pleasure of the Almighty God.</li>
        <li>To express the righteousness of God in all operations, products and services as our brand.</li>
        <li>To treat our staff as valued partners (co-owner) in the business.</li>
        <li>To work in such a way that will preserve the earth resources.</li>
      </ul>
      <h2>Corporate Culture</h2>
      <h3>Quality Culture</h3>
      <p>Kelvara Oil and Gas Limited pride itself on its corporate quality culture. We feel strongly that quality goes beyond simply following procedures and meeting productivity expectations.</p>
      <p>At every level of the company, we insist on taking quality focused action and transferring those values to our clients. The culture of quality is part of our environment. The end result is better communication, high-end services and products that function as promised.</p>
      <p>Each member of the Kelvara team is empowered and expected to make good decisions based on the need to deliver quality and value.</p>
    </div>
  </section>

  <section class="page page--right">
    <svg class="band" width="560" height="230" viewBox="0 0 560 230">
      <defs>
        <linearGradient id="photoTone" x1="0" y1="0" x2="1" y2="1">
          <stop offset="0" stop-color="#a9c3d6"/>
          <stop offset=".55" stop-color="#6f8d74"/>
          <stop offset="1" stop-color="#3d5c46"/>
        </linearGradient>
      </defs>
      <path d="M0,150 C180,125 380,80 560,25" fill="none" stroke="var(--orange)" stroke-width="9"/>
      <path d="M0,160 C180,135 380,90 560,35" fill="none" stroke="#fff" stroke-width="6"/>
      <path d="M0,166 C180,141 380,96 560,41 L560,230 L0,230 Z" fill="var(--green)"/>
      <path d="M0,215 C200,200 380,175 560,140 L560,230 L0,230 Z" fill="var(--green-dark)" opacity=".35"/>
      <g role="img" aria-label="Photo of green pipeline valves and fittings">
        <circle cx="70" cy="160" r="42" fill="url(#photoTone)" stroke="#fff" stroke-width="3"/>
      </g>
      <g role="img" aria-label="Photo of technicians on site inspecting equipment">
        <circle cx="182" cy="132" r="42" fill="url(#photoTone)" stroke="#fff" stroke-width="3"/>
      </g>
      <g role="img" aria-label="Photo of a large wheel valve on a gas line">
        <circle cx="308" cy="96" r="44" fill="url(#photoTone)" stroke="#fff" stroke-width="3"/>
      </g>
      <g role="img" aria-label="Photo of red pumps and piping at a plant">
        <circle cx="438" cy="62" r="44" fill="url(#photoTone)" stroke="#fff" stroke-width="3"/>
      </g>
    </svg>
    <div class="site-pill">www.kelvaraoilandgas.example</div>
    <div class="content">
      <h2>Health, Safety and Environment (HSE)</h2>
      <p>Health, Safety and Environment (HSE) is a fundamental component of KOGL business principles and corporate culture. It is our priority to maintain safe and healthy working conditions by ensuring industrial and work area safety rules, regulations, laws, conditions and standard codes.</p>
      <p>The company believes that effective management of HSE affairs not only protects staff and environment, but also contributes to the company’s success. Therefore, we regard it as important as the achievement of any other key business objective.</p>
      <h2>Products</h2>
      <h3>Equipment Hire</h3>
      <p>We use state of the art equipment to deliver prompt services according to specifications. We also support the industry and grow local capacity by offering equipment hire and lease services. We have in stock an array of pre-mobbed equipment, ready to be deployed for emergency and planned activity.</p>
      <h2>Services</h2>
      <p>Kelvara Oil and Gas Limited is functional in both the downstream and upstream operation. Whatever your need, we have the expertise to offer solutions and guidance.</p>
      <ul class="services">
        <li><svg viewBox="0 0 10 10"><path d="M1 5.5 L4 8.5 L9 1.5" fill="none" stroke="var(--tick)" stroke-width="2"/></svg>Pipeline and flow lines design, construction/installation, maintenance and emergency repairs.</li>
        <li><svg viewBox="0 0 10 10"><path d="M1 5.5 L4 8.5 L9 1.5" fill="none" stroke="var(--tick)" stroke-width="2"/></svg>Installation &amp; maintenance of booster pumps and platform refurbishment.</li>
        <li><svg viewBox="0 0 10 10"><path d="M1 5.5 L4 8.5 L9 1.5" fill="none" stroke="var(--tick)" stroke-width="2"/></svg>Maintenance and rehabilitation of platforms, gas compressor plants and flow stations.</li>
        <li><svg viewBox="0 0 10 10"><path d="M1 5.5 L4 8.5 L9 1.5" fill="none" stroke="var(--tick)" stroke-width="2"/></svg>Engineering Design Services. Procurement Services. Provide experienced and professional technical Manpower.</li>
        <li><svg viewBox="0 0 10 10"><path d="M1 5.5 L4 8.5 L9 1.5" fill="none" stroke="var(--tick)" stroke-width="2"/></svg>Installation &amp; maintenance of steam and gas turbines, boilers &amp; heat exchangers, fire water system, pumps, etc.</li>
        <li><svg viewBox="0 0 10 10"><path d="M1 5.5 L4 8.5 L9 1.5" fill="none" stroke="var(--tick)" stroke-width="2"/></svg>Engineering Services (Mechanical, Civil and Electrical works). Environmental Services.</li>
      </ul>
      <p>We can execute fully integrated projects at remote locations supported by a satellite office. Our team work diligently to maximize clients’ return and avoid unplanned downtime. We have the requisite equipment to deliver value and quality.</p>
    </div>
  </section>
</div>
</body>
</html>
```